Author needs a new book, Kindle and Audiobook cover design

I updated and re-edited a book I wrote 25 years ago but now realize the title and design did not get the job done. I am seeking a book, Kindle and audiobook design that will make me stand out. The final design will pop while being sensitive to the nature of the subject. The title of the book is Quiet Lanterns. Subtitle: Ways to Notice and Step Away From Harmful Circles While Keeping Steady Belief by Dorian T. Wexcombe. I am wanting to get the attention of people who have been damaged by a church relationship that started well but ended badly.
Updates

The book title is: Quiet Lanterns. The Subtitle is: Ways To Notice and Step Away From Harmful Circles While Keeping Steady Belief. The dimension is 6x9 (150 pages) and I am the author: Dorian T. Wexcombe

Target Market(s)

People with a church experience; church leadership. Religious abuse victims.

Industry/Entity Type

Christian

Font styles to use
Serif

Colors

Designer to choose colors to be used in the design.

Requirements
Nice to have
• I am not married to the Serif font if another design works better.

```html
<!DOCTYPE html>
<html lang="en">
<head>
<meta charset="utf-8">
<title>Quiet Lanterns — Dorian T. Wexcombe</title>
<link rel="stylesheet" href="https://fonts.googleapis.com/css2?family=Andika:wght@400;700&family=Sorts+Mill+Goudy&display=swap">
<style>
  :root {
    --backdrop: #d6d6d6;
    --navy: #0c1436;
    --sky-teal: #5f9a86;
    --sky-gold: #e2d25a;
    --haze-yellow: #c9c456;
    --dusk-purple: #3e2a58;
    --title-white: #ffffff;
    --subtitle-ink: #141414;
    --author-gold: #f1d77a;
  }
  html, body {
    margin: 0;
    padding: 0;
    width: 1200px;
    height: 1200px;
    overflow: hidden;
    background: var(--backdrop);
  }
  .canvas {
    position: relative;
    width: 1200px;
    height: 1200px;
  }
  .book-cover {
    position: absolute;
    left: 249px;
    top: 45px;
    width: 702px;
    height: 1110px;
    background: var(--navy);
    overflow: hidden;
    box-shadow: 0 6px 18px rgba(0, 0, 0, 0.28);
  }
  .cover-photo {
    position: absolute;
    inset: 0 0 auto 0;
    height: 900px;
    background:
      linear-gradient(180deg, rgba(12,20,54,0) 70%, var(--navy) 100%),
      linear-gradient(180deg,
        var(--sky-teal) 0%,
        #9fb462 18%,
        var(--sky-gold) 38%,
        var(--haze-yellow) 50%,
        #7a6a4a 62%,
        var(--dusk-purple) 74%,
        #2a2440 86%,
        var(--navy) 100%);
  }
  .cover-title {
    position: absolute;
    left: 0;
    right: 0;
    top: 52px;
    margin: 0;
    text-align: center;
    font-family: "Andika", sans-serif;
    font-weight: 400;
    font-size: 118px;
    line-height: 128px;
    letter-spacing: 3px;
    color: var(--title-white);
    text-shadow: 3px 4px 6px rgba(20, 30, 20, 0.55);
  }
  .cover-subtitle {
    position: absolute;
    left: 0;
    right: 0;
    top: 304px;
    margin: 0;
    text-align: center;
    font-family: "Sorts Mill Goudy", serif;
    font-weight: 400;
    font-size: 25px;
    line-height: 35px;
    letter-spacing: 0.5px;
    color: var(--subtitle-ink);
  }
  .cover-author {
    position: absolute;
    left: 0;
    right: 0;
    top: 960px;
    margin: 0;
    text-align: center;
    font-family: "Sorts Mill Goudy", serif;
    font-weight: 400;
    font-size: 48px;
    letter-spacing: 1.5px;
    color: var(--author-gold);
  }
</style>
</head>
<body>
  <main class="canvas">
    <section class="book-cover">
      <div class="cover-photo" role="img" aria-label="Photograph of a man sitting alone on the ground at sunset, head bowed, under a golden-green sky with grasses around him"></div>
      <h1 class="cover-title">Quiet<br>Lanterns</h1>
      <p class="cover-subtitle">Ways to Notice and Step Away From Harmful Circles<br>While Keeping Steady Belief</p>
      <p class="cover-author">Dorian T. Wexcombe</p>
    </section>
  </main>
</body>
</html>
```